Brivora Collective Business Card Design

We need a business card design for Brivora Collective. We are a healthcare recruiting, wellness and education company. We partner with medical facilities to find quality candidates. We also offer free wellness courses.
The final design should communicate an emphasis on recruiting and wellness
The main purpose of the business card is to utilized it for networking events, give to hospitals, executives, VCs surgery centers and clinics. I want it to be sleek, clean, use of our brand colors and professional.

```html
<!DOCTYPE html>
<html lang="en">
<head>
<meta charset="utf-8">
<title>Brivora Collective – Business Card</title>
<link href="https://fonts.googleapis.com/css2?family=Mulish:wght@400;700&display=swap" rel="stylesheet">
<style>
  :root {
    --brand-green: #035a4e;
    --card-white: #ffffff;
    --backdrop: #e6e6e6;
    --ink-light: #ffffff;
  }
  * { box-sizing: border-box; margin: 0; padding: 0; }
  html, body {
    width: 1200px; height: 1200px; overflow: hidden;
    background: var(--backdrop);
    font-family: "Mulish", sans-serif;
  }
  .canvas { position: relative; width: 1200px; height: 1200px; }
  .card {
    position: absolute; left: 188px; width: 825px; height: 509px;
    background: var(--card-white);
    box-shadow: 6px 8px 10px rgba(0,0,0,0.22);
    overflow: hidden;
  }
  .card--front { top: 70px; }
  .card--back { top: 623px; }

  .front-panel { position: absolute; inset: 0; width: 825px; height: 509px; }

  .front-brand {
    position: absolute; left: 62px; top: 175px; width: 300px;
    text-align: center; color: var(--brand-green);
    font-weight: 400; font-size: 50px; line-height: 1.1; letter-spacing: 0.5px;
  }

  .contact { position: absolute; right: 56px; color: var(--ink-light); text-align: right; }
  .contact__name { top: 112px; font-weight: 700; font-size: 35px; letter-spacing: 0.3px; line-height: 1; }
  .contact__role { top: 164px; font-size: 21px; line-height: 1; }
  .contact__line {
    position: absolute; right: 56px; color: var(--ink-light);
    font-size: 20.5px; line-height: 1; display: flex; align-items: center; gap: 14px;
  }
  .contact__line svg { width: 16px; height: 16px; fill: var(--ink-light); flex: none; }
  .contact__line--phone { top: 240px; }
  .contact__line--email { top: 273px; }
  .contact__line--address { top: 334px; }
  .contact__city { position: absolute; right: 86px; top: 368px; color: var(--ink-light); font-size: 20.5px; line-height: 1; }

  .back-brand {
    position: absolute; left: 0; right: 0; top: 112px;
    display: flex; flex-direction: column; align-items: center; gap: 40px;
    color: var(--brand-green);
  }
  .back-brand__mark { width: 104px; height: 104px; background: var(--brand-green); }
  .back-brand__name {
    font-weight: 400; font-size: 54px; line-height: 1.05; letter-spacing: 0.5px;
    text-align: center;
  }
</style>
</head>
<body>
<main class="canvas">
  <section class="card card--front">
    <svg class="front-panel" viewBox="0 0 825 509" aria-hidden="true">
      <polygon fill="var(--brand-green)" points="548,0 825,0 825,370 685,509 413,509 413,136"/>
    </svg>
    <div class="front-brand">Brivora<br>Collective</div>

    <div class="contact contact__name">YOUR NAME</div>
    <div class="contact contact__role">Designation</div>

    <div class="contact__line contact__line--phone">
      <span>555-274-6190</span>
      <svg viewBox="0 0 24 24" aria-hidden="true"><path d="M6.6 10.8a15.1 15.1 0 0 0 6.6 6.6l2.2-2.2c.3-.3.7-.4 1-.2 1.1.4 2.3.6 3.6.6.6 0 1 .4 1 1V20c0 .6-.4 1-1 1A17 17 0 0 1 3 4c0-.6.4-1 1-1h3.5c.6 0 1 .4 1 1 0 1.3.2 2.5.6 3.6.1.3 0 .7-.2 1z"/></svg>
    </div>
    <div class="contact__line contact__line--email">
      <span>mailid@brivoramail.com</span>
      <svg viewBox="0 0 24 24" aria-hidden="true"><path d="M3 5h18a1 1 0 0 1 1 1v12a1 1 0 0 1-1 1H3a1 1 0 0 1-1-1V6a1 1 0 0 1 1-1zm9 7.5L20 7H4z"/></svg>
    </div>
    <div class="contact__line contact__line--address">
      <span>000 Harbor Crest Drive Suite 00</span>
      <svg viewBox="0 0 24 24" aria-hidden="true"><path d="M12 2a7 7 0 0 0-7 7c0 5.2 7 13 7 13s7-7.8 7-13a7 7 0 0 0-7-7zm0 9.5A2.5 2.5 0 1 1 12 6.5a2.5 2.5 0 0 1 0 5z"/></svg>
    </div>
    <div class="contact__city">Lakeview Bay, FL 34012</div>
  </section>

  <section class="card card--back">
    <div class="back-brand">
      <div class="back-brand__mark" aria-hidden="true"></div>
      <div class="back-brand__name">Brivora<br>Collective</div>
    </div>
  </section>
</main>
</body>
</html>
```